Mezzanine Floor Manufacturer looking for a new business card design

We manufacture mezzanine floors and are providers of racking systems. We provide a range of items/services - simple rack repairs , full warehouse fit outs , manufacturer and install mezzanine floors , partitioning and large turnkey projects. Recently had a new website - www.corrowden-racking.co.uk and would like our business cards updating aswell . Our current card is single sided in the old logo colours (pdf attached) and needs updating.

Target Market(s)

We deal with large projects/ multi national companies and also smaller projects and companies throughout the UK ranging from a single warehouse to a large multi site company.

Industry/Entity Type

Business

Contact Information for Business Card

Will have job title,tel no's, email ,website address etc like example pdf

Requirements
Must have
• Hi - needs to use the colours of the logo & new website. Card needs to be professional

```html
<!DOCTYPE html>
<html lang="en">
<head>
<meta charset="utf-8">
<title>Corrowden Racking – Business Card</title>
<link rel="stylesheet" href="https://fonts.googleapis.com/css2?family=Arimo:wght@400;700&display=swap">
<style>
  :root {
    --backdrop: #6f6e70;
    --card-base: #e6e6e6;
    --card-stripe: #f2f2f2;
    --brand-red: #d0262d;
    --brand-red-deep: #a3121a;
    --band-edge: #b4b4b4;
    --ink: #1c1c1c;
    --ink-soft: #333333;
    --white: #ffffff;
  }
  * { margin: 0; padding: 0; box-sizing: border-box; }
  html, body { width: 1059px; height: 1200px; overflow: hidden; }
  body {
    background: var(--backdrop);
    font-family: "Arimo", Arial, sans-serif;
    position: relative;
  }
  .card {
    position: absolute;
    left: 89px;
    width: 880px;
    height: 507px;
    box-shadow: 0 10px 28px rgba(0,0,0,0.35);
  }
  .card--front { top: 70px; }
  .card--back { top: 630px; }
  .card svg { display: block; width: 100%; height: 100%; }
  .t-company { font-weight: 700; fill: var(--ink); font-size: 23px; }
  .t-company-sub { font-weight: 700; fill: var(--ink); font-size: 13.5px; }
  .t-band-name { font-weight: 700; fill: var(--white); font-size: 22px; letter-spacing: 1px; }
  .t-person { font-weight: 700; fill: var(--brand-red); font-size: 18px; }
  .t-role { fill: var(--ink); font-size: 15px; letter-spacing: 0.5px; }
  .t-mobile { fill: var(--ink-soft); font-size: 12px; }
  .t-phone { fill: var(--ink-soft); font-size: 11px; letter-spacing: 0.8px; }
  .t-web { fill: var(--ink); font-size: 15px; }
  .t-service { fill: var(--ink); font-size: 16px; }
  .t-address { fill: var(--white); font-size: 15px; letter-spacing: 0.6px; }
</style>
</head>
<body>

<section class="card card--front" aria-label="Business card front">
  <svg viewBox="0 0 422 243" xmlns="http://www.w3.org/2000/svg">
    <defs>
      <linearGradient id="red-fill" x1="0" y1="0" x2="1" y2="1">
        <stop offset="0" stop-color="var(--brand-red)"/>
        <stop offset="1" stop-color="var(--brand-red-deep)"/>
      </linearGradient>
      <clipPath id="front-clip"><rect width="422" height="243"/></clipPath>
    </defs>
    <g clip-path="url(#front-clip)">
      <rect class="card-base" width="422" height="243" fill="var(--card-base)"/>
      <g class="diagonal-stripes" fill="var(--card-stripe)" opacity="0.8">
        <polygon points="190,0 250,0 422,150 422,210"/>
        <polygon points="270,0 320,0 422,90 422,130"/>
        <polygon points="110,60 150,60 360,243 320,243"/>
        <polygon points="40,110 80,110 230,243 190,243"/>
      </g>
      <ellipse class="band-edge" cx="100" cy="36" rx="160" ry="100" fill="var(--band-edge)"/>
      <ellipse class="band-red" cx="95" cy="30" rx="150" ry="95" fill="url(#red-fill)"/>
      <text class="t-band-name" x="105" y="62" text-anchor="middle">CORROWDEN</text>

      <text class="t-company" x="414" y="59" text-anchor="end">CORROWDEN</text>
      <text class="t-company-sub" x="414" y="82" text-anchor="end">RACKING</text>

      <text class="t-person" x="321" y="126" text-anchor="middle">Daniel Hartley</text>
      <line x1="250" y1="131" x2="392" y2="131" stroke="var(--ink-soft)" stroke-width="1"/>
      <text class="t-role" x="326" y="148" text-anchor="middle">Technical Sales</text>
      <text class="t-mobile" x="326" y="163" text-anchor="middle">Mob: 07700 900318</text>

      <text class="t-phone" x="7" y="212">Tel:  01632 960481</text>
      <text class="t-phone" x="7" y="227">Fax: 01632 960492</text>

      <text class="t-web" x="414" y="209" text-anchor="end">daniel@corrowden-racking.co.uk</text>
      <text class="t-web" x="414" y="228" text-anchor="end">www.corrowden-racking.co.uk</text>
    </g>
  </svg>
</section>

<section class="card card--back" aria-label="Business card back">
  <svg viewBox="0 0 422 243" xmlns="http://www.w3.org/2000/svg">
    <defs>
      <linearGradient id="red-fill-back" x1="0" y1="0" x2="1" y2="1">
        <stop offset="0" stop-color="var(--brand-red)"/>
        <stop offset="1" stop-color="var(--brand-red-deep)"/>
      </linearGradient>
      <clipPath id="back-clip"><rect width="422" height="243"/></clipPath>
    </defs>
    <g clip-path="url(#back-clip)">
      <rect class="card-base" width="422" height="243" fill="var(--card-base)"/>
      <g class="service-rows" fill="var(--card-stripe)" opacity="0.8">
        <rect x="0" y="30" width="422" height="30"/>
        <rect x="0" y="90" width="422" height="30"/>
        <rect x="0" y="150" width="422" height="30"/>
        <rect x="0" y="210" width="422" height="33"/>
      </g>
      <ellipse class="band-edge" cx="330" cy="265" rx="210" ry="130" fill="var(--band-edge)"/>
      <ellipse class="band-red" cx="340" cy="275" rx="208" ry="128" fill="url(#red-fill-back)"/>

      <g class="services">
        <text class="t-service" x="10" y="24">Mezzanine Floors</text>
        <text class="t-service" x="10" y="54">Cantilever Racking</text>
        <text class="t-service" x="10" y="84">Pallet Racking</text>
        <text class="t-service" x="10" y="114">Longspan shelving</text>
        <text class="t-service" x="10" y="144">Steel Shelving</text>
        <text class="t-service" x="10" y="174">Safety Barriers</text>
        <text class="t-service" x="250" y="24">Partitioning</text>
        <text class="t-service" x="250" y="54">Turnkey Projects</text>
      </g>

      <g class="address">
        <text class="t-address" x="410" y="180" text-anchor="end">Seven Mill Close</text>
        <text class="t-address" x="410" y="199" text-anchor="end">Ashbrook Trade Park</text>
        <text class="t-address" x="410" y="218" text-anchor="end">Hallworth, Derbyshire DE9 4QP</text>
      </g>
    </g>
  </svg>
</section>

</body>
</html>
```